Plumbing & Heating company

A leaflet containing -

Company name - Brackenfold Plumbing Solutions
logo
Mobile number - 07700 914226
Landline - 01632 870512
Email - Info@brackenfoldplumbing.example.co.uk
website - Brackenfold-plumbing.example.co.uk
Social media logos - pixgram, Chatterly

services we offer

- Boiler replacements (free quote)
- General plumbing & heating
- Tap replacements
- 1st & 2nd
- New builds & Extensions
- Cylinder replcemets

```html
<!DOCTYPE html>
<html lang="en">
<head>
<meta charset="utf-8">
<title>Brackenfold Plumbing Solutions – Leaflet</title>
<link rel="stylesheet" href="https://fonts.googleapis.com/css2?family=Anton&family=Mulish:wght@700;800&family=Open+Sans:wght@300;400&display=swap">
<style>
  :root {
    --page-bg: #ececec;
    --charcoal: #383c40;
    --slate: #464a52;
    --white: #ffffff;
    --orange: #f07a2a;
    --navy: #2e3a8c;
    --gold: #e0b04a;
    --ink: #333333;
    --link-blue: #1a5a9e;
    --badge-grey: #e6e7e9;
    --rule-grey: #c8c8c8;
  }
  * { box-sizing: border-box; margin: 0; padding: 0; }
  html, body { width: 1115px; height: 1200px; overflow: hidden; background: var(--page-bg); }
  .leaflet {
    position: absolute; left: 106px; top: 19px;
    width: 960px; height: 1235px;
    transform: scale(0.94); transform-origin: 0 0;
    background: var(--white);
    box-shadow: 0 6px 18px rgba(0,0,0,0.15);
    overflow: hidden;
  }
  .abs { position: absolute; }
  .hero-panel { left: 0; top: 0; width: 440px; height: 595px; background: var(--charcoal); }
  .hero-title {
    left: 0; top: 72px; width: 440px; text-align: center;
    font-family: "Anton", sans-serif; font-size: 74px; line-height: 77px;
    color: var(--white); white-space: nowrap; letter-spacing: 0.5px;
  }
  .intro-box { left: 60px; top: 329px; width: 320px; height: 239px; background: var(--slate); text-align: center; padding-top: 28px; }
  .intro-heading { font-family: "Anton", sans-serif; font-size: 26px; line-height: 35px; color: var(--orange); white-space: nowrap; }
  .intro-text { margin-top: 10px; font-family: "Open Sans", sans-serif; font-weight: 300; font-size: 24px; line-height: 31px; color: var(--white); }
  .hero-photo { left: 440px; top: 0; width: 520px; height: 595px;
    background: linear-gradient(180deg, #3f78c4 0%, #a9c6e6 18%, #8a5a36 30%, #a06a40 55%, #9a9490 75%, #8d8a88 100%); }
  .gallery-photo { top: 637px; height: 259px; }
  .photo-bathroom { left: 58px; width: 213px; background: linear-gradient(160deg, #e8e8e8, #c9cbcd 70%, #b8b9ba); }
  .photo-utility { left: 285px; width: 210px; background: linear-gradient(180deg, #c8bca6 0%, #d9d4cc 40%, #3a3a3a 58%, #bdbdbd 80%, #e5e5e5); }
  .photo-sink-unit { left: 509px; width: 200px; background: linear-gradient(180deg, #f0f0f0 0%, #b9a583 60%, #cdb48e 100%); }
  .photo-kitchen { left: 722px; width: 179px; background: linear-gradient(180deg, #ededea 0%, #dcdcdc 45%, #2b2b2b 65%, #d0d0d0 100%); }
  .services-heading { left: 47px; top: 930px; font-family: "Anton", sans-serif; font-size: 28px; line-height: 34px; color: var(--navy); letter-spacing: 0.3px; }
  .services-rule { left: 291px; top: 948px; width: 380px; height: 2px; background: var(--gold); }
  .service-list { list-style: none; font-family: "Mulish", sans-serif; font-weight: 800; font-size: 20px; line-height: 30.5px; color: var(--ink); }
  .service-list li { display: flex; align-items: center; gap: 10px; white-space: nowrap; }
  .service-list li::before { content: ""; width: 16px; height: 16px; border-radius: 50%;
    background: radial-gradient(circle at 35% 35%, #f7b84a, #d9811a 70%, #b8650e); flex: none; }
  .list-left { left: 48px; top: 978px; }
  .list-right { left: 408px; top: 979px; }
  .accreditation-panel { left: 714px; top: 924px; width: 187px; height: 187px; background: var(--badge-grey); }
  .badge-installer { left: 758px; top: 936px; width: 95px; height: 94px; background: #ffffff; border: 2px solid #2e8b57; }
  .badge-safety { left: 738px; top: 1036px; width: 136px; height: 54px; background: linear-gradient(90deg, #1f3a78 60%, #f5d90a 60%); border: 1px solid #1f3a78; }
  .footer-rule { left: 47px; top: 1110px; width: 667px; height: 2px; background: var(--rule-grey); }
  .web-icon { left: 48px; top: 1130px; }
  .web-block { left: 110px; top: 1136px; font-family: "Mulish", sans-serif; }
  .web-address { font-size: 19px; font-weight: 800; color: var(--link-blue); white-space: nowrap; }
  .web-caption { font-size: 17px; font-weight: 800; color: #111; margin-top: 4px; }
  .social-box { left: 480px; top: 1128px; width: 102px; height: 64px; background: var(--badge-grey);
    display: flex; flex-direction: column; justify-content: center; align-items: center; gap: 3px;
    font-family: "Mulish", sans-serif; font-weight: 800; font-size: 13px; color: var(--ink); }
  .phone-icon { left: 620px; top: 1124px; }
  .phone-number { left: 678px; top: 1120px; font-family: "Anton", sans-serif; font-size: 40px; line-height: 50px; color: var(--ink); letter-spacing: 0.5px; }
  .email-line { right: 55px; top: 1173px; display: flex; align-items: center; gap: 6px;
    font-family: "Mulish", sans-serif; font-weight: 800; font-size: 13px; color: #111; white-space: nowrap; }
  .colour-band-warm { left: 0; top: 1205px; width: 535px; height: 30px; background: linear-gradient(90deg, #f7b21b, #f26c2f 55%, #e8373f); }
  .colour-band-cool { left: 535px; top: 1205px; width: 425px; height: 30px; background: linear-gradient(90deg, #1560a0, #1a9bd7); }
</style>
</head>
<body>
<main class="leaflet">
  <section class="abs hero-panel"></section>
  <h1 class="abs hero-title">BRACKENFOLD<br>PLUMBING<br>SOLUTIONS</h1>
  <div class="abs intro-box">
    <h2 class="intro-heading">BRACKENFOLD PLUMBING &amp;<br>HEATING CONTRACTOR</h2>
    <p class="intro-text">Based in Hampshire and<br>covering Winchester and<br>the surrounding areas.</p>
  </div>
  <div class="abs hero-photo" role="img" aria-label="Photo of a newly built timber-clad house with solar panels under a blue sky"></div>

  <div class="abs gallery-photo photo-bathroom" role="img" aria-label="Photo of a finished bathroom with shower, basin and toilet"></div>
  <div class="abs gallery-photo photo-utility" role="img" aria-label="Photo of a utility room with boiler, sink and washing machine"></div>
  <div class="abs gallery-photo photo-sink-unit" role="img" aria-label="Photo of pipework and filter installed under a sink"></div>
  <div class="abs gallery-photo photo-kitchen" role="img" aria-label="Photo of a kitchen with stainless steel sink and dishwasher"></div>

  <h2 class="abs services-heading">SERVICES WE OFFER</h2>
  <div class="abs services-rule"></div>
  <ul class="abs service-list list-left">
    <li>Boiler replacements (Free Quote)</li>
    <li>General plumbing &amp; heating</li>
    <li>Tap replacements</li>
  </ul>
  <ul class="abs service-list list-right">
    <li>1st &amp; 2nd</li>
    <li>New builds &amp; Extensions</li>
    <li>Cylinder replcemets</li>
  </ul>

  <div class="abs accreditation-panel"></div>
  <div class="abs badge-installer" aria-hidden="true"></div>
  <div class="abs badge-safety" aria-hidden="true"></div>

  <div class="abs footer-rule"></div>
  <svg class="abs web-icon" width="56" height="56" viewBox="0 0 56 56" aria-hidden="true">
    <g fill="none" stroke="#111" stroke-width="2.5">
      <circle cx="28" cy="28" r="25"/>
      <ellipse cx="28" cy="28" rx="11" ry="25"/>
      <line x1="28" y1="3" x2="28" y2="53"/>
      <path d="M7 15 H49 M7 41 H49"/>
    </g>
    <rect x="4" y="21" width="48" height="14" rx="7" fill="#111"/>
    <text x="28" y="32" text-anchor="middle" font-family="Mulish, sans-serif" font-weight="800" font-size="11" fill="#fff">www</text>
  </svg>
  <div class="abs web-block">
    <div class="web-address">Brackenfold-plumbing.example.co.uk</div>
    <div class="web-caption">Visit our website</div>
  </div>
  <div class="abs social-box">
    <span>Chatterly</span>
    <span>pixgram</span>
  </div>
  <svg class="abs phone-icon" width="48" height="48" viewBox="0 0 48 48" aria-hidden="true">
    <circle cx="24" cy="24" r="24" fill="#f07a2a"/>
    <path d="M11 21 C11 14 37 14 37 21 L37 24 L31 24 L31 20 L17 20 L17 24 L11 24 Z" fill="#fff"/>
    <path d="M15 25 L19 22 L29 22 L33 25 L33 34 L15 34 Z" fill="#fff"/>
    <circle cx="24" cy="28.5" r="3" fill="#f07a2a"/>
  </svg>
  <div class="abs phone-number">01632 870512</div>
  <div class="abs email-line">
    <svg width="14" height="10" viewBox="0 0 14 10" aria-hidden="true">
      <rect width="14" height="10" fill="#111"/>
      <path d="M0 0 L7 6 L14 0" fill="none" stroke="#fff" stroke-width="1.2"/>
    </svg>
    <span>Info@brackenfoldplumbing.example.co.uk</span>
  </div>

  <div class="abs colour-band-warm"></div>
  <div class="abs colour-band-cool"></div>
</main>
</body>
</html>
```